Business Card design
Cordavera Ruvek Martial Arts Training Center
I need single sided standard sized Business Card [3.5" x 2"]
Font in logo is CGF Locust Resistance. This font does not need to be used.
Modern
Cordavera Ruvek or Cordavera Ruvek Martial Arts Training Center
Martial Arts Discipline | Athletic Excellence
2671 Bramble Rd
Kalamazoo, MI
info@cordaverix.example
www.cordaverix.example
facebook.com/cordaverix
optional items for the business card:
Pelnor Grappling League
Todd Weslin Jiu Jitsu
Orvane Kickboxing Union
Mixed Martial Arts
Fitness
Can put the logo on one side and the information on the second side if you would like to submit that type of design.
Cordavera Ruvek illustrator file
Cordavera Ruvek eps file

```html
<!DOCTYPE html>
<html lang="en">
<head>
<meta charset="utf-8">
<title>Cordavera Ruvek Business Card</title>
<link href="https://fonts.googleapis.com/css2?family=PT+Sans:wght@400;700&display=swap" rel="stylesheet">
<style>
  :root {
    --brand-red: #ee4036;
    --brand-grey: #7b7b7b;
    --paper: #ffffff;
    --stage: #ffffff;
    --line: #d9d9d9;
  }
  * { margin: 0; padding: 0; box-sizing: border-box; }
  html, body {
    width: 1200px; height: 721px; overflow: hidden;
    background: var(--stage);
    font-family: "PT Sans", Arial, sans-serif;
  }
  .sheet { position: relative; width: 1200px; height: 721px; }
  .card {
    position: absolute; width: 556px; height: 324px;
    overflow: hidden; border: 1px solid var(--line);
  }
  .card--front { left: 36px; top: 29px; background: var(--paper); }
  .card--red { left: 606px; top: 29px; background: var(--brand-red); border-color: var(--brand-red); }
  .card--grey { left: 322px; top: 366px; background: var(--brand-grey); border-color: var(--brand-grey); }

  .wordmark {
    display: flex; align-items: center; gap: 10px;
    font-weight: 700; font-size: 30px; letter-spacing: 1px;
    text-transform: uppercase; white-space: nowrap;
  }
  .wordmark__square { width: 22px; height: 22px; flex: none; }
  .card--front .wordmark { position: absolute; left: 22px; top: 48px; color: var(--brand-red); }
  .card--front .wordmark__square { background: var(--brand-grey); }
  .card--red .wordmark, .card--grey .wordmark {
    position: absolute; left: 50%; top: 50%; transform: translate(-50%, -50%);
  }
  .card--red .wordmark { color: var(--paper); }
  .card--red .wordmark__square { background: var(--brand-grey); }
  .card--grey .wordmark { color: var(--paper); }
  .card--grey .wordmark__square { background: var(--brand-red); }

  .tagline {
    position: absolute; right: 16px; top: 124px;
    text-align: right; color: var(--brand-red);
    font-size: 21px; line-height: 36px;
  }
  .diagonal { position: absolute; left: 0; top: 0; width: 556px; height: 324px; }
  .contact {
    position: absolute; left: 22px; top: 244px;
    color: var(--paper); font-size: 12.5px; line-height: 18px;
  }
</style>
</head>
<body>
<main class="sheet">
  <section class="card card--front">
    <div class="wordmark"><span class="wordmark__square"></span>Cordavera Ruvek</div>
    <div class="tagline">
      <p>Martial Arts Discipline</p>
      <p>Athletic Excellence</p>
    </div>
    <svg class="diagonal" viewBox="0 0 556 324" aria-hidden="true">
      <polygon points="0,172 556,262 556,324 0,324" fill="var(--brand-grey)"/>
      <polygon points="0,152 556,241 556,250 0,161" fill="var(--brand-red)"/>
    </svg>
    <div class="contact">
      <p>2671 Bramble Rd, Kalamazoo, MI 49001</p>
      <p>Phone: 269-555-0148 | Cell: 269-555-0193</p>
      <p>Email: info@cordaverix.example | www.cordaverix.example</p>
    </div>
  </section>

  <section class="card card--red">
    <div class="wordmark"><span class="wordmark__square"></span>Cordavera Ruvek</div>
  </section>

  <section class="card card--grey">
    <div class="wordmark"><span class="wordmark__square"></span>Cordavera Ruvek</div>
  </section>
</main>
</body>
</html>
```